business stationery for email layout
startup company
Simple
RT
Via G. Morelli, 17
26813 Codogno LO
Italy
Info@Tallimora.com
www.tallimora.com
minimalist, retail, fashion, technology, internet, innovative,one-step ahead, easy, intuitive, immediate, serious,credible
logo blue version
logo grey version
symbol blue version
symbol grey version

```html
<!DOCTYPE html>
<html lang="en">
<head>
<meta charset="utf-8">
<title>Tallimora business cards</title>
<link href="https://fonts.googleapis.com/css2?family=Montserrat:wght@700&family=Arimo:wght@400&display=swap" rel="stylesheet">
<style>
  :root {
    --backdrop: #6b3f1d;
    --card: #ffffff;
    --brand-navy: #1f4474;
    --text-grey: #4a4a4a;
    --rule-grey: #b9b9b9;
    --figure-deep: #2f62b3;
    --figure-light: #9fd0ee;
  }
  html, body {
    margin: 0;
    padding: 0;
    width: 1200px;
    height: 367px;
    overflow: hidden;
    background: var(--backdrop);
  }
  .stage {
    position: relative;
    width: 1200px;
    height: 367px;
  }
  .card {
    position: absolute;
    background: var(--card);
    border-radius: 22px;
    box-shadow: 0 2px 6px rgba(0,0,0,0.35);
  }
  .card-front { left: 24px; top: 29px; width: 564px; height: 314px; }
  .card-back  { left: 643px; top: 36px; width: 538px; height: 300px; }
  .brand-name {
    position: absolute;
    margin: 0;
    font-family: "Montserrat", sans-serif;
    font-weight: 700;
    color: var(--brand-navy);
    letter-spacing: 1px;
    line-height: 1;
  }
  .card-front .brand-name { left: 20px; top: 40px; font-size: 58px; }
  .card-back .brand-name  { left: 0; right: 0; top: 44px; font-size: 64px; text-align: center; }
  .contact {
    position: absolute;
    left: 26px;
    top: 132px;
    font-family: "Arimo", sans-serif;
    color: var(--text-grey);
  }
  .contact .initials {
    margin: 0 0 8px;
    font-size: 26px;
    color: #2a2a2a;
  }
  .contact p {
    margin: 0;
    font-size: 14.5px;
    line-height: 19.5px;
  }
  .divider {
    position: absolute;
    left: 268px;
    top: 170px;
    width: 1px;
    height: 140px;
    background: var(--rule-grey);
  }
  .figure {
    position: absolute;
    border-radius: 48% 52% 44% 56%;
    background: radial-gradient(ellipse at 45% 40%, var(--figure-deep) 0%, #5a98d4 45%, var(--figure-light) 75%, rgba(255,255,255,0) 100%);
  }
  .card-front .figure { left: 290px; top: 118px; width: 240px; height: 168px; }
  .card-back .figure  { left: 200px; top: 150px; width: 128px; height: 92px; }
  .web {
    position: absolute;
    left: 0; right: 0; top: 252px;
    text-align: center;
    font-family: "Arimo", sans-serif;
    font-size: 14px;
    color: var(--text-grey);
  }
</style>
</head>
<body>
<div class="stage">
  <section class="card card-front">
    <h1 class="brand-name">TALLIMORA</h1>
    <div class="figure" role="img" aria-label="Illustration of a leaping figure carrying a shopping bag, in blue tones"></div>
    <div class="divider"></div>
    <div class="contact">
      <p class="initials">RT</p>
      <p>Via G. Morelli, 17, 26813</p>
      <p>Codogno LO, Italy</p>
      <p>P : +390245118260</p>
      <p>F : +390245118261</p>
      <p>E : Info@Tallimora.com</p>
      <p>W : www.tallimora.com</p>
    </div>
  </section>
  <section class="card card-back">
    <h2 class="brand-name">TALLIMORA</h2>
    <div class="figure" role="img" aria-label="Small illustration of a leaping figure with a shopping bag, in blue tones"></div>
    <p class="web">www.tallimora.com</p>
  </section>
</div>
</body>
</html>
```